Landscape Construction and Design Company

We are a landscape construction and design company from New Jersey. We design and install landscapes and hardscapes for residential properties. The name of the company is Corwin's Landscape and Design LLC. We specialize mostly in planting trees and stone work, some water features. We would like to see design themes that include a tree or trees and a stone walkway or wall. We like earth tone colors. We like traditional to modern designs.

Target Market(s)

Homeowners

Industry/Entity Type

Landscape

Contact Information for Business Card

Nature themed design, earth tone colors, space for company name, address, phone numbers, email and website address

Logo Text

No text

Font styles to use
Serif

Colors

Designer to choose colors to be used in the design.

Requirements
Must have
• A tree or trees, similar to the ones uploaded in my supporting images
Nice to have
• I like trees similar to those in my uploaded supporting images. I like artistic, nature theme, earth tone colors
Should not have
• Pictures of real landscapes, cartoon looking logo or objects

```html
<!DOCTYPE html>
<html lang="en">
<head>
<meta charset="utf-8">
<title>Corwin's Landscape and Design LLC — Business Card</title>
<link rel="stylesheet" href="https://fonts.googleapis.com/css2?family=Cinzel:wght@400&family=Cormorant+Garamond:wght@500&family=Cabin:wght@400&display=swap">
<style>
  :root {
    --page-bg: #ffffff;
    --card-bg: #fdfadb;
    --card-edge: #efeccf;
    --ink: #7a6a53;
    --leaf-light: #d7e8a8;
    --leaf-mid: #a9cf86;
    --leaf-deep: #8fbf7a;
    --mist: #b9b7c8;
    --water: #9dd3dc;
  }
  * { box-sizing: border-box; margin: 0; padding: 0; }
  html, body {
    width: 1200px; height: 1200px; overflow: hidden;
    background: var(--page-bg);
  }
  .card {
    position: absolute;
    left: 136px; top: 322px;
    width: 928px; height: 555px;
    background: var(--card-bg);
    border: 1px solid var(--card-edge);
    color: var(--ink);
  }
  .tree-artwork {
    position: absolute;
    left: 29px; top: 78px;
    width: 400px; height: 350px;
    border-radius: 48% 52% 20% 20% / 55% 55% 12% 12%;
    background:
      radial-gradient(ellipse at 50% 35%, var(--mist) 0%, transparent 45%),
      radial-gradient(ellipse at 75% 40%, var(--leaf-deep) 0%, transparent 55%),
      radial-gradient(ellipse at 20% 60%, #f3f0a6 0%, transparent 50%),
      linear-gradient(180deg, var(--leaf-mid) 0%, var(--leaf-light) 70%, var(--water) 100%);
  }
  .brand {
    position: absolute; right: 50px; text-align: right; white-space: nowrap;
    font-weight: 400;
  }
  .brand-name {
    top: 84px;
    font-family: 'Cinzel', serif;
    font-size: 58px; line-height: 1;
    letter-spacing: 0.2em; margin-right: -0.2em;
  }
  .brand-tagline {
    top: 150px;
    font-family: 'Cinzel', serif;
    font-size: 29px; line-height: 1;
  }
  .holder {
    position: absolute; right: 50px; top: 214px; text-align: right;
    font-family: 'Cormorant Garamond', serif;
    font-size: 30px; line-height: 36px; text-transform: uppercase;
  }
  .contact-list {
    position: absolute; right: 50px; top: 305px;
    list-style: none;
    font-family: 'Cabin', sans-serif; font-size: 24px;
  }
  .contact-item {
    display: flex; align-items: center; gap: 14px;
    height: 38px; margin-bottom: 2px;
  }
  .contact-item svg { width: 30px; height: 30px; flex: none; }
  .services {
    position: absolute; left: 0; right: 0; top: 450px;
    text-align: center;
    font-family: 'Cabin', sans-serif; font-size: 23px; line-height: 29px;
  }
</style>
</head>
<body>
  <main class="card">
    <div class="tree-artwork" role="img" aria-label="Watercolour illustration of three trees on a green hill above a blue stream"></div>

    <h1 class="brand brand-name">CORWIN'S</h1>
    <p class="brand brand-tagline">Landscape and Design LLC</p>

    <p class="holder">Lena Marsh Holloway<br>CEO / Owner</p>

    <ul class="contact-list">
      <li class="contact-item">
        <svg viewBox="0 0 24 24" aria-hidden="true"><path fill="var(--ink)" d="M6.6 10.8a15.1 15.1 0 0 0 6.6 6.6l2.2-2.2c.3-.3.7-.4 1-.2 1.1.4 2.300.6 3.6.6.6 0 1 .4 1 1V20c0 .6-.4 1-1 1A17 17 0 0 1 3 4c0-.6.4-1 1-1h3.5c.6 0 1 .4 1 1 0 1.3.2 2.5.6 3.6.1.3 0 .7-.2 1z"/></svg>
        <span>+44 (0) 70184 52637</span>
      </li>
      <li class="contact-item">
        <svg viewBox="0 0 24 24" aria-hidden="true"><rect x="3" y="6" width="18" height="12" fill="var(--ink)"/><path d="M3 6l9 7 9-7M3 18l7-6M21 18l-7-6" stroke="var(--card-bg)" stroke-width="1.5" fill="none"/></svg>
        <span>lmh@corwinsl&amp;d.com</span>
      </li>
      <li class="contact-item">
        <svg viewBox="0 0 24 24" aria-hidden="true"><circle cx="12" cy="12" r="10" fill="var(--ink)"/><path d="M2 12h20M12 2c3 3 3 17 0 20M12 2c-3 3-3 17 0 20" stroke="var(--card-bg)" stroke-width="1.2" fill="none"/></svg>
        <span>www.corwinsl&amp;d.com</span>
      </li>
    </ul>

    <p class="services">
      Custom Woods | stone and tile | Community Based Craftspeople Green Building |<br>
      Tree Management and Protection|Rain Gardens | Living roofs | Custom Renovations |<br>
      Sustainable / Renewable Resources
    </p>
  </main>
</body>
</html>
```